Cover Page for our 2021 Comprehensive Needs Assessment Report 3 ring binder

Create a cover for our 2021 Comprehensive Needs Assessment. This is a report full of survey and non survey data, used for decision making. Modern Colors. Logo is attached as well as 2020 cover for easy explanation. However we do not want the same cover as last year, it should have a new color scheme for this year and a new look with the same feel.

Target Market(s)

School Districts

```html
<!DOCTYPE html>
<html lang="en">
<head>
<meta charset="utf-8">
<title>Comprehensive Needs Assessment 2021 – Cover</title>
<link rel="stylesheet" href="https://fonts.googleapis.com/css2?family=Barlow:wght@400;500;600&family=Barlow+Condensed:wght@600&family=Barlow+Semi+Condensed:wght@600;700&display=swap">
<style>
  :root {
    --backdrop: #c4c6c8;
    --navy: #172a36;
    --navy-soft: #1d3443;
    --orange: #f8960f;
    --orange-deep: #f08300;
    --white: #ffffff;
    --photo-warm: #c89a62;
    --photo-light: #e2c08e;
  }
  * { margin: 0; padding: 0; box-sizing: border-box; }
  html, body { width: 1200px; height: 972px; overflow: hidden; }
  body { background: var(--backdrop); position: relative; }

  .cover {
    position: absolute;
    left: 337px;
    top: 36px;
    width: 525px;
    height: 900px;
    background: var(--navy);
    overflow: hidden;
    box-shadow: 0 12px 30px rgba(0,0,0,0.25);
  }
  .cover-art { position: absolute; inset: 0; width: 100%; height: 100%; }

  .publisher {
    position: absolute;
    top: 54px;
    right: 46px;
    display: flex;
    align-items: center;
    gap: 7px;
    font-family: "Barlow", sans-serif;
    font-weight: 500;
    font-size: 15px;
    line-height: 1.05;
    color: var(--navy);
  }
  .publisher-dot { width: 10px; height: 10px; border-radius: 50%; background: var(--navy); }

  .report-title { position: absolute; left: 40px; top: 505px; }
  .report-title .kicker {
    font-family: "Barlow Condensed", sans-serif;
    font-weight: 600;
    font-size: 21px;
    color: var(--white);
    letter-spacing: 0.5px;
    line-height: 1;
  }
  .report-title .headline {
    font-family: "Barlow Semi Condensed", sans-serif;
    font-weight: 700;
    font-size: 50px;
    color: var(--orange);
    line-height: 1;
    margin-top: 4px;
  }
  .report-title .subline {
    font-family: "Barlow Semi Condensed", sans-serif;
    font-weight: 700;
    font-size: 23px;
    color: var(--orange);
    line-height: 1;
    margin-top: 2px;
    letter-spacing: 0.3px;
  }

  .district { position: absolute; left: 38px; top: 668px; }
  .district .district-name {
    font-family: "Barlow", sans-serif;
    font-weight: 600;
    font-size: 66px;
    color: var(--white);
    line-height: 1;
    letter-spacing: 0.5px;
  }
  .district .district-label {
    font-family: "Barlow", sans-serif;
    font-weight: 400;
    font-size: 23px;
    color: var(--orange);
    line-height: 1;
    margin-top: 2px;
    margin-left: 2px;
  }

  .report-year {
    position: absolute;
    right: 36px;
    top: 772px;
    font-family: "Barlow", sans-serif;
    font-weight: 600;
    font-size: 58px;
    color: var(--white);
    line-height: 1;
  }
  .year-rule {
    position: absolute;
    left: 40px;
    right: 36px;
    top: 832px;
    height: 3px;
    background: var(--white);
  }
</style>
</head>
<body>
  <main class="cover">
    <svg class="cover-art" viewBox="0 0 525 900" xmlns="http://www.w3.org/2000/svg">
      <defs>
        <linearGradient id="photoTone" x1="0" y1="0" x2="1" y2="1">
          <stop offset="0" stop-color="#8a6a4e"/>
          <stop offset="0.45" stop-color="#d2a56b"/>
          <stop offset="0.75" stop-color="#e6c896"/>
          <stop offset="1" stop-color="#b88a55"/>
        </linearGradient>
      </defs>

      <!-- orange upper band with navy corner -->
      <polygon points="200,0 525,0 525,260" fill="var(--orange)"/>
      <polygon points="300,0 525,0 525,180" fill="var(--orange-deep)" opacity="0.5"/>
      <polygon points="420,0 525,0 525,78" fill="var(--navy)"/>
      <!-- navy stripe and white rule along top diagonal -->
      <polygon points="250,40 525,250 525,268 248,56" fill="var(--navy)"/>
      <polygon points="245,44 525,258 525,264 241,49" fill="var(--white)"/>

      <!-- orange left wedge -->
      <polygon points="0,340 110,420 0,500" fill="var(--orange)"/>
      <!-- orange lower-right wedge -->
      <polygon points="340,640 525,505 525,760" fill="var(--orange)"/>
      <polygon points="420,700 525,620 525,760" fill="var(--orange-deep)" opacity="0.6"/>

      <!-- photo area -->
      <polygon role="img" aria-label="Photo: team at a wooden desk reviewing printed charts and a tablet"
        points="0,0 200,0 525,265 525,492 345,626 85,408 0,468" fill="url(#photoTone)"/>

      <!-- white rules framing photo -->
      <polygon points="0,462 85,402 88,410 0,474" fill="var(--white)"/>
      <polygon points="340,628 525,490 525,500 348,634" fill="var(--white)"/>
    </svg>

    <div class="publisher">
      <span class="publisher-dot"></span>
      <span>Brightpath<br>Learning, LLC</span>
    </div>

    <div class="report-title">
      <div class="kicker">COMPREHENSIVE</div>
      <div class="headline">NEEDS</div>
      <div class="subline">ASSESSMENT</div>
    </div>

    <div class="district">
      <div class="district-name">RIDGEVIEW</div>
      <div class="district-label">SCHOOL DISTRICT</div>
    </div>

    <div class="report-year">2021</div>
    <div class="year-rule"></div>
  </main>
</body>
</html>
```